Mobile grocery convenience store app

PantryVan is a mobile grocery store. Customers should be able to request the grocery bus to their home address. See where the bus is with map and estimated time. Put multiple people requests in order they request. Give an 15 min -20 min per stop for customers to come aboard bus and shops/pay for for their grocery. Must have log in for bus driver/clerk to sign in and see get directions to next address in que and info they would need. Such as contact for customer should driver get lost. Similar to zova and Kemo. Special instructions for handicap so driver can bring items to door. Products we sale should be able to be added or changed easily by manager or sign in.
Updates

Problem starting design contest. Was never supposed to be 6 days. Thanks

Industry/Entity Type

Grocery

Font styles to use
Sans Serif

Colors
0255a3
fee18a
fece3e

Requirements
Must have
• Colors match as close to logo colors

```html
<!DOCTYPE html>
<html lang="en">
<head>
<meta charset="utf-8">
<title>PantryVan – App Screens</title>
<link href="https://fonts.googleapis.com/css2?family=Karla:wght@400;500;700&family=Nunito+Sans:wght@400;600&display=swap" rel="stylesheet">
<style>
:root{
  --yellow:#fbbd2c;
  --yellow-soft:#fee18a;
  --yellow-deep:#fece3e;
  --blue:#0255a3;
  --map:#2b2c2e;
  --panel:#2f2f30;
  --ink:#1d1d1d;
  --field:#eeeff1;
  --white:#ffffff;
  --muted:#8a8a8a;
}
*{box-sizing:border-box;margin:0;padding:0}
html,body{width:1200px;height:649px;overflow:hidden;background:var(--white)}
body{position:relative;font-family:"Karla",sans-serif;color:var(--ink)}
.abs{position:absolute}
.section-title{position:absolute;top:14px;font-family:"Nunito Sans",sans-serif;font-size:23px;font-weight:400;letter-spacing:.3px}
.caption{position:absolute;font-family:"Nunito Sans",sans-serif;font-size:6.5px}
.screen{position:absolute;overflow:hidden}
.map{position:absolute;inset:0;background:linear-gradient(160deg,#353638,#252628 70%,#2d2e30)}
.status{position:absolute;top:6px;left:10px;right:8px;display:flex;justify-content:space-between;font-size:5px;font-weight:700}
.avatar{position:absolute;border-radius:50%;background:var(--white);box-shadow:0 1px 3px rgba(0,0,0,.4)}
.pill{position:absolute;background:var(--yellow);border-radius:12px;color:var(--ink)}
/* splash */
.splash{left:52px;top:66px;width:124px;height:268px;background:#f1f1f2;box-shadow:0 1px 3px rgba(0,0,0,.25)}
.brand{position:absolute;top:129px;left:0;right:0;display:flex;align-items:center;justify-content:center;gap:4px;font-size:13px;font-weight:500;color:var(--blue)}
.brand-dot{width:8px;height:8px;border-radius:50%;background:var(--yellow)}
.home-bar{position:absolute;bottom:4px;left:50%;width:42px;height:1.5px;margin-left:-21px;border-radius:2px}
/* phones */
.phone{left:266px;width:124px;height:268px}
.phone .status{color:var(--white)}
.stop-pill{left:30px;top:20px;width:90px;height:23px;padding:4px 0 0 9px;font-size:5px;line-height:7px;font-weight:500}
.loc-dot{position:absolute;width:8px;height:8px;border-radius:50%;background:var(--yellow);border:1px solid #c68a00}
.request-btn{position:absolute;left:8px;top:229px;width:106px;height:18px;border-radius:10px;background:var(--yellow);font-size:5.6px;font-weight:700;display:flex;align-items:center;justify-content:center;letter-spacing:.2px}
.arrive-pill{left:7px;top:187px;width:85px;height:17px;display:flex;align-items:center;justify-content:center;font-size:6px;font-weight:500}
.access{position:absolute;border-radius:50%;background:#2f7fe6;border:1px solid var(--white)}
.sheet{position:absolute;left:4px;right:4px;top:216px;bottom:0;background:var(--white);border-radius:6px 6px 0 0;padding:14px 7px 0}
.sheet-handle{position:absolute;top:5px;left:50%;width:16px;height:1.5px;margin-left:-8px;background:var(--yellow)}
.sheet h3{font-size:8px;font-weight:700}
.tabs{display:flex;gap:9px;margin-top:7px;font-size:3.8px;color:var(--muted);letter-spacing:.2px}
.tabs .on{color:var(--ink);font-weight:700}
.sheet-cards{display:flex;gap:8px;margin-top:6px}
.sheet-cards span{flex:1;height:10px;border-radius:3px;background:var(--field)}
/* tablet */
.tablet{left:484px;top:66px;width:338px;height:253px}
.timer{left:42px;top:14px;width:90px;height:23px;padding:4px 0 0 9px;font-size:7px;line-height:8px;font-weight:700}
.chip{position:absolute;top:19px;height:12px;border-radius:7px;background:var(--white);font-size:5.5px;display:flex;align-items:center;gap:3px;padding:0 5px}
.queue-title{position:absolute;left:19px;top:51px;font-size:15px;font-weight:700;color:var(--yellow)}
.add-chip{left:77px;top:54px}
.stack{position:absolute;left:22px;width:104px;border-radius:8px;background:#d99a14}
.stop-card{position:absolute;left:16px;top:75px;width:116px;height:124px;border-radius:8px;background:var(--yellow);padding:9px 8px 0}
.stop-card h2{font-size:12px;line-height:11.5px;font-weight:500}
.stop-name{font-size:8px;margin-top:3px;display:flex;align-items:center;gap:4px}
.stop-card hr{border:0;border-top:.6px solid #c68a00;margin:6px -8px 0}
.stop-note{font-size:5.4px;font-weight:700;line-height:6px;margin-top:7px;color:#4a3300}
.stop-note+hr{margin:5px 0 0}
.btn-soft{position:absolute;height:15px;border-radius:8px;background:var(--yellow-deep);font-size:6px;display:flex;align-items:center;justify-content:center;box-shadow:0 .5px 2px rgba(0,0,0,.2)}
.nav-btn{position:absolute;left:22px;top:218px;width:106px;height:19px;border-radius:10px;background:var(--yellow);font-size:5.6px;font-weight:700;display:flex;align-items:center;justify-content:center;letter-spacing:.2px}
/* inventory */
.inventory{left:835px;top:66px;width:337px;height:253px;background:var(--panel)}
.inv-head{position:absolute;left:0;top:0;right:0;height:46px;background:var(--yellow)}
.back{position:absolute;left:3px;top:19px;font-size:5px}
.inv-title{position:absolute;left:6px;top:29px;font-size:11px;font-weight:700}
.add-product{position:absolute;left:276px;top:26px;width:50px;height:12px;border-radius:7px;background:var(--white);font-size:5.6px;display:flex;align-items:center;justify-content:center;gap:2px}
.produce{position:absolute;left:9px;top:61px;font-size:12px;color:var(--white)}
.search{position:absolute;left:149px;top:62px;width:113px;height:12px;border-radius:2px;background:#3a3a3b;color:#8d8d8d;font-size:5px;padding:3px 0 0 10px}
.sort{position:absolute;left:274px;top:64px;font-size:5.4px;color:var(--white);display:flex;gap:3px;align-items:center}
.card{position:absolute;width:47px;height:54px;background:#f7f7f7;border-radius:3px;overflow:hidden}
.card .thumb{position:absolute;left:7px;top:5px;width:33px;height:26px;border-radius:6px}
.thumb.banana{background:radial-gradient(ellipse at 50% 55%,#f9c93a,#f2b21d 60%,#f7f7f7 72%)}
.thumb.berry{background:radial-gradient(ellipse at 50% 50%,#d9262b,#b5171d 55%,#f7f7f7 72%)}
.card b{position:absolute;left:5px;top:38px;font-size:5px;font-weight:400;color:#555}
.card i{position:absolute;left:5px;top:45px;font-size:3.6px;font-style:normal;color:#aaa}
/* modals */
.blurred{position:absolute;left:484px;top:360px;width:338px;height:253px;background:#161616;overflow:hidden}
.blur-shape{position:absolute;filter:blur(5px)}
.modal{position:absolute;background:var(--white);border-radius:6px;box-shadow:0 2px 8px rgba(0,0,0,.4)}
.close{position:absolute;font-size:9px;font-weight:700;line-height:1}
.label{position:absolute;left:8px;font-size:4.2px;color:#555;letter-spacing:.3px}
.field{position:absolute;left:7px;width:102px;height:15px;border-radius:3px;background:var(--field);font-size:5.8px;font-weight:700;padding:4px 5px 0}
.toggle{position:absolute;right:3px;top:3px;width:17px;height:9px;border-radius:5px;background:var(--yellow)}
.toggle::after{content:"";position:absolute;right:1px;top:1px;width:7px;height:7px;border-radius:50%;background:var(--white)}
.add-tile{position:absolute;left:11px;top:123px;width:40px;height:46px;border-radius:3px;background:#f2f3f4;color:var(--yellow);font-size:16px;display:flex;align-items:center;justify-content:center;font-weight:300}
.modal-btn{position:absolute;left:5px;top:181px;width:105px;height:15px;border-radius:8px;background:var(--yellow);font-size:6px;display:flex;align-items:center;justify-content:center}
.stepper{position:absolute;right:4px;top:2px;display:flex;border:.6px solid var(--yellow);border-radius:2px}
.stepper span{width:15px;height:10px;font-size:8px;line-height:9px;text-align:center;color:#d99a14}
.stepper span+span{border-left:.6px solid var(--yellow)}
</style>
</head>
<body>

<h1 class="section-title" style="left:267px">Customer Views</h1>
<h1 class="section-title" style="left:484px">Driver/Manager Views</h1>

<!-- Splash -->
<section class="screen splash">
  <div class="status"><span>9:41</span><span>▮▮ ◠ ▬</span></div>
  <div class="brand"><span class="brand-dot"></span>PantryVan</div>
  <div class="home-bar" style="background:#d8d8d8"></div>
</section>

<!-- Customer home -->
<section class="screen phone" style="top:66px">
  <div class="map" role="img" aria-label="Dark street map of the neighbourhood showing the van's position"></div>
  <div class="status"><span>9:41</span><span>▮▮ ◠ ▬</span></div>
  <div class="avatar" style="left:4px;top:21px;width:21px;height:21px"></div>
  <div class="pill stop-pill">Currently at 128 Alder St.<br>15 minutes until next stop.</div>
  <div class="loc-dot" style="left:47px;top:165px"></div>
  <div class="request-btn">REQUEST PANTRYVAN</div>
  <div class="home-bar" style="background:var(--white)"></div>
</section>
<p class="caption" style="left:266px;top:337px">Home Screen</p>

<!-- Customer bus requested -->
<section class="screen phone" style="top:359px">
  <div class="map" role="img" aria-label="Dark street map with the van's route to the customer"></div>
  <div class="status"><span>9:41</span><span>▮▮ ◠ ▬</span></div>
  <div class="avatar" style="left:4px;top:21px;width:21px;height:21px"></div>
  <div class="pill stop-pill">Currently at 128 Alder St.<br>15 minutes until next stop.</div>
  <svg class="abs" style="left:0;top:0" width="124" height="268"><polyline points="71,104 71,147 50,147 50,172" fill="none" stroke="#fbbd2c" stroke-width="1"/></svg>
  <div class="loc-dot" style="left:46px;top:170px"></div>
  <div class="pill arrive-pill">Arriving at 10:00am</div>
  <div class="access" style="left:101px;top:188px;width:16px;height:16px">
    <svg width="14" height="14" viewBox="0 0 14 14"><circle cx="7" cy="3.5" r="1.2" fill="#fff"/><path d="M6.5 5v3h3l1 2.5M6 6.5a3 3 0 1 0 3 4" fill="none" stroke="#fff" stroke-width="1"/></svg>
  </div>
  <div class="sheet">
    <span class="sheet-handle"></span>
    <svg class="abs" style="right:7px;top:14px" width="8" height="8" viewBox="0 0 8 8"><circle cx="3.3" cy="3.3" r="2.5" fill="none" stroke="#222" stroke-width=".8"/><path d="M5.2 5.2 7.4 7.4" stroke="#222" stroke-width=".8"/></svg>
    <h3>Browse Groceries</h3>
    <div class="tabs"><span class="on">PRODUCE</span><span>MEATS</span><span>SNACKS</span><span>BEVERAGES</span></div>
    <div class="sheet-cards"><span></span><span></span></div>
  </div>
</section>
<p class="caption" style="left:266px;top:630px">Home Screen (Bus Requested)</p>

<!-- Driver tablet -->
<section class="screen tablet">
  <div class="map" role="img" aria-label="Dark street map with the next stop marked"></div>
  <div class="avatar" style="left:17px;top:16px;width:19px;height:19px"></div>
  <div class="pill timer">9:23 remaining until<br>next stop.</div>
  <div class="chip" style="left:213px;width:66px">☰ Manage Inventory</div>
  <div class="chip" style="left:293px;width:32px"><span style="width:5px;height:5px;border-radius:50%;background:#3fc43a"></span>Online</div>
  <div class="queue-title">Queue</div>
  <div class="chip add-chip" style="top:54px;width:55px">＋ Add Customer</div>
  <div class="stack" style="top:190px;height:20px;opacity:.85"></div>
  <div class="stack" style="top:185px;height:20px;left:19px;width:110px;background:#e6a818"></div>
  <article class="stop-card">
    <h2>128 Alder<br>Street</h2>
    <div class="stop-name">Maya Torres
      <span class="access" style="position:relative;display:inline-block;width:10px;height:10px"></span></div>
    <hr>
    <p class="stop-note">Customer requests groceries<br>delivered to door.</p>
    <hr>
  </article>
  <div class="btn-soft" style="left:22px;top:155px;width:104px">Contact Customer</div>
  <div class="btn-soft" style="left:22px;top:177px;width:50px">View Order</div>
  <div class="btn-soft" style="left:76px;top:177px;width:50px">Directions</div>
  <div class="nav-btn">NAVIGATE TO NEXT STOP</div>
  <div class="loc-dot" style="left:232px;top:118px;background:#f2a127;box-shadow:0 0 0 3px rgba(242,161,39,.3)"></div>
</section>
<p class="caption" style="left:484px;top:324px">Home Screen (Driver Tablet)</p>

<!-- Manage inventory -->
<section class="screen inventory">
  <div class="inv-head">
    <span class="back">‹ Back</span>
    <span class="inv-title">Manage Inventory</span>
    <span class="add-product">＋ Add Product</span>
  </div>
  <div class="produce">Produce</div>
  <div class="search">Search</div>
  <div class="sort">⬍ Sort By Category</div>

  <div class="card" style="left:9px;top:84px"><div class="thumb banana" role="img" aria-label="Bananas"></div><b>Bananas</b><i>70¢/lb</i></div>
  <div class="card" style="left:77px;top:84px"><div class="thumb berry" role="img" aria-label="Strawberries"></div><b>Strawberries</b><i>$3.50</i></div>
  <div class="card" style="left:145px;top:84px"><div class="thumb banana" role="img" aria-label="Bananas"></div><b>Bananas</b><i>70¢/lb</i></div>
  <div class="card" style="left:212px;top:84px"><div class="thumb berry" role="img" aria-label="Strawberries"></div><b>Strawberries</b><i>$3.50</i></div>
  <div class="card" style="left:280px;top:84px"><div class="thumb banana" role="img" aria-label="Bananas"></div><b>Bananas</b><i>70¢/lb</i></div>

  <div class="card" style="left:9px;top:145px"><div class="thumb banana" role="img" aria-label="Bananas"></div><b>Bananas</b><i>70¢/lb</i></div>
  <div class="card" style="left:77px;top:145px"><div class="thumb berry" role="img" aria-label="Strawberries"></div><b>Strawberries</b><i>$3.50</i></div>
  <div class="card" style="left:145px;top:145px"><div class="thumb banana" role="img" aria-label="Bananas"></div><b>Bananas</b><i>70¢/lb</i></div>
  <div class="card" style="left:212px;top:145px"><div class="thumb berry" role="img" aria-label="Strawberries"></div><b>Strawberries</b><i>$3.50</i></div>
  <div class="card" style="left:280px;top:145px"><div class="thumb banana" role="img" aria-label="Bananas"></div><b>Bananas</b><i>70¢/lb</i></div>

  <div class="card" style="left:9px;top:206px"><div class="thumb banana" role="img" aria-label="Bananas"></div><b>Bananas</b><i>70¢/lb</i></div>
  <div class="card" style="left:77px;top:206px"><div class="thumb berry" role="img" aria-label="Strawberries"></div><b>Strawberries</b><i>$3.50</i></div>
  <div class="card" style="left:145px;top:206px"><div class="thumb banana" role="img" aria-label="Bananas"></div><b>Bananas</b><i>70¢/lb</i></div>
  <div class="card" style="left:212px;top:206px"><div class="thumb berry" role="img" aria-label="Strawberries"></div><b>Strawberries</b><i>$3.50</i></div>
  <div class="card" style="left:280px;top:206px"><div class="thumb banana" role="img" aria-label="Bananas"></div><b>Bananas</b><i>70¢/lb</i></div>
</section>
<p class="caption" style="left:835px;top:324px">Manage Inventory</p>

<!-- Add customer modal -->
<section class="blurred">
  <div class="blur-shape" style="left:16px;top:20px;width:120px;height:22px;border-radius:12px;background:#4a3a10"></div>
  <div class="blur-shape" style="left:16px;top:75px;width:116px;height:124px;border-radius:8px;background:#4d3b0c"></div>
  <div class="blur-shape" style="left:22px;top:218px;width:106px;height:19px;border-radius:10px;background:#4d3b0c"></div>
  <div class="modal" style="left:111px;top:26px;width:115px;height:202px">
    <span class="close" style="right:7px;top:8px">✕</span>
    <span class="label" style="top:15px">DETAILS</span>
    <div class="field" style="top:25px">Name</div>
    <div class="field" style="top:44px">Phone Number</div>
    <div class="field" style="top:63px">Address</div>
    <div class="field" style="top:83px">Requires Delivery to Door<span class="toggle"></span></div>
    <div class="abs" style="left:7px;right:6px;top:104px;border-top:.6px solid #ddd"></div>
    <span class="abs" style="left:12px;top:111px;font-size:5.8px;font-weight:700">Order Items</span>
    <div class="add-tile">+</div>
    <div class="modal-btn">Add Customer to Queue</div>
  </div>
</section>
<p class="caption" style="left:484px;top:617px">Add Customer to Queue Manually</p>

<!-- Edit product modal -->
<section class="blurred" style="left:835px;top:359px;width:337px;background:#1c1c1c">
  <div class="blur-shape" style="left:0;top:0;width:337px;height:46px;background:#5a4410"></div>
  <div class="blur-shape" style="left:9px;top:84px;width:320px;height:160px;background:repeating-linear-gradient(90deg,#3c3c3c 0 47px,transparent 47px 68px)"></div>
  <div class="modal" style="left:82px;top:24px;width:115px;height:202px">
    <span class="close" style="right:6px;top:8px">✕</span>
    <div class="abs" role="img" aria-label="Packaged strawberries" style="left:11px;top:20px;width:92px;height:59px;border-radius:6px;background:radial-gradient(ellipse at 50% 50%,#d9262b,#a9141a 70%,#e9e9ea)"></div>
    <span class="label" style="top:89px">NAME</span>
    <div class="field" style="top:95px;width:101px">Strawberries</div>
    <span class="label" style="top:117px">PRICE</span>
    <div class="field" style="top:123px;width:101px">3.50<span style="position:absolute;right:5px">$</span></div>
    <span class="label" style="top:145px">CATEGORY</span>
    <div class="field" style="top:150px;width:101px">Produce</div>
    <span class="label" style="top:173px">STOCK</span>
    <div class="field" style="top:178px;width:101px">86<span class="stepper"><span>−</span><span>+</span></span></div>
  </div>
</section>
<p class="caption" style="left:835px;top:617px">Manage Inventory (Add/Edit Product)</p>

</body>
</html>
```